BRIGHTDESK - Remote Tech Support Site

We are looking for a new very responsive and simple website for our brand Brightdesk.com - a remote technical support company.

This company supports customers Globally in different countries throughout Eur/ North America / South America / Asia etc (please keep this in mind and integrate into the idea).

Its important to us that the design is very explanatory, the customer should easily be able to figure out that we provide computer support right away ... I like one page responsive type designs as well without a bunch of menu items

Here are some similar sites we like - but still looking for a unique design that fits out brand "brightdesk" - I have upload also some layouts i like (but the designs are not important just the layouts), youll see it includes consumer business etc which is important.

VOLM.COM - I love how clean it is - nice and white easy to see everything

PLUMWIRE247.COM - also nice the layout and responsive one page design makes it easy to use

corvalfix.com - similar to plumwire design as well - you can get the idea im looking for between the two

You will notice those examples are much different then the attachments I added - again this is more of an idea for possible layouts .. attached is also the logo - could inspire color scheme / blue white black etc

Target Market(s)

Home consumers without computer knowledge , older age 45-65, small medium business ... computer repair - slow computers

Industry/Entity Type

Computer Repair

Logo Text

Brightdesk

Coding

Coded - Design and coding required

Number of Pages Required

1 page

Font styles to use
Sans Serif
Other font styles liked:
• your choice responsive

Colors

Designer to choose colors to be used in the design.

Requirements
Must have
• Clean - responsive - professional design - the name says it all - brightdesk
• CALL TO ACTIONS FOR "Get Help Now!" / "Learn More" etc
Nice to have
• We are looking for a new very responsive and simple website for our brand Brightdesk.com - a remote technical support company.
• This company supports customers Globally in different countries throughout Eur/ North America / South America / Asia etc (please keep this in mind and integrate into the idea).
• Its important to us that the design is very explanatory, the customer should easily be able to figure out that we provide computer support right away ... I like one page responsive type designs as well without a bunch of menu items
• Here are some similar sites we like - but still looking for a unique design that fits out brand "brightdesk" - I have upload also some layouts i like (but the designs are not important just the layouts), youll see it includes consumer business etc which is important.
• VOLM.COM - I love how clean it is - nice and white easy to see everything
• PLUMWIRE247.COM - also nice the layout and responsive one page design makes it easy to use
• corvalfix.com - similar to plumwire design as well - you can get the idea im looking for between the two
Should not have
• dark, packed page - bad small font -

```html
<!DOCTYPE html>
<html lang="en">
<head>
<meta charset="utf-8">
<title>Brightdesk – Remote Tech Support</title>
<link rel="stylesheet" href="https://fonts.googleapis.com/css2?family=Montserrat:wght@400;500;600;700&family=Lato:ital,wght@0,400;0,700;1,400&display=swap">
<style>
:root{
  --blue:#1a7de6;
  --blue-deep:#0f63c9;
  --blue-light:#3a97f2;
  --ink:#1b1b1b;
  --black:#111;
  --grey-text:#666;
  --line:#e3e3e3;
  --card:#f1f1f1;
  --hero-bg:#dfe6ee;
  --white:#fff;
}
*{box-sizing:border-box;margin:0;padding:0}
html,body{width:1200px;height:3719px;overflow:hidden}
body{position:relative;background:var(--white);font-family:"Lato",sans-serif;color:var(--ink)}
.abs{position:absolute}
.heading{font-family:"Montserrat",sans-serif}

/* top bar */
.topbar{top:0;left:0;width:1200px;height:50px;background:var(--black);color:#fff;font-family:"Montserrat",sans-serif;font-size:14px;font-weight:600}
.topbar .contact{position:absolute;left:74px;top:16px;display:flex;gap:28px;align-items:center}
.topbar .contact span{display:flex;align-items:center;gap:8px}
.topbar .lang{position:absolute;left:955px;top:16px;display:flex;gap:6px;align-items:center}
.topbar .login{position:absolute;left:1040px;top:11px;width:86px;height:28px;background:#fff;color:var(--blue);border-radius:3px;text-align:center;line-height:28px;font-size:12px;font-weight:700}

/* hero */
.hero{top:50px;left:0;width:1200px;height:540px;background:linear-gradient(90deg,#eef2f6 0%,#e2e9f0 45%,#c9d3de 100%)}
.hero-photo{position:absolute;left:508px;top:86px;width:620px;height:404px;background:linear-gradient(180deg,#d6dee8 0%,#b7c4d3 60%,#8ea1b8 100%)}
.nav{top:64px;left:74px;width:1052px;height:82px;background:var(--blue)}
.brand{position:absolute;left:14px;top:22px;display:flex;align-items:center;gap:10px;color:#fff;font-family:"Montserrat",sans-serif;font-size:28px;font-weight:500}
.brand .dot{width:34px;height:34px;border-radius:50%;background:#fff}
.menu{position:absolute;right:14px;top:24px;display:flex;gap:6px;font-family:"Montserrat",sans-serif;font-size:14px;font-weight:600;color:#fff}
.menu a{padding:10px 18px;color:#fff;text-decoration:none}
.menu a.active{background:var(--black)}
.hero h1{position:absolute;left:74px;top:180px;font-family:"Montserrat",sans-serif;font-weight:700;font-size:37px;line-height:50px;letter-spacing:.5px;color:var(--black)}
.hero h1 .accent{color:var(--blue);font-size:42px;display:block}
.btn{position:absolute;height:46px;font-family:"Montserrat",sans-serif;font-size:14px;font-weight:700;text-align:center;line-height:46px;border-radius:3px}
.btn-dark{background:var(--black);color:#fff}
.btn-outline{border:2px solid var(--blue);color:var(--blue);line-height:42px;background:transparent}
.btn-blue{background:var(--blue);color:#fff}
.hero-dots{position:absolute;left:74px;top:382px;display:flex;gap:6px}
.hero-dots i{width:9px;height:9px;border-radius:50%;background:#8a97a6}
.hero-dots i:first-child{background:var(--blue)}

/* pricing */
.pricing{top:540px;left:74px;width:1052px;height:928px;background:#fff;box-shadow:0 4px 18px rgba(0,0,0,.08);border-radius:4px}
.section-title{font-family:"Montserrat",sans-serif;font-weight:600;font-size:26px;text-align:center;letter-spacing:.3px;color:var(--black)}
.pricing .section-title{position:absolute;top:44px;left:0;width:100%}
.plans{position:absolute;left:35px;top:122px;width:982px;height:721px;display:flex;box-shadow:0 2px 10px rgba(0,0,0,.12)}
.plan{flex:0 0 auto;position:relative;border-right:1px solid #ddd;text-align:center}
.plan:last-child{border-right:none}
.plan-head{height:50px;background:#222;color:#fff;font-family:"Montserrat",sans-serif;font-weight:600;font-size:17px;line-height:50px}
.plan-photo{height:206px;background:linear-gradient(160deg,#e8edf2,#b9c6d4)}
.price{margin-top:32px;font-family:"Montserrat",sans-serif;color:var(--blue);font-weight:600;display:flex;justify-content:center;align-items:flex-start}
.price sup{font-size:32px;line-height:38px}
.price b{font-size:62px;line-height:62px;font-weight:600}
.price em{font-style:italic;font-size:13px;color:#333;font-family:"Lato",sans-serif;margin-top:34px;margin-left:4px}
.setup{font-style:italic;font-size:13px;color:#444;margin-top:6px}
.features{list-style:none;margin:24px 28px 0}
.features li{font-size:14px;color:#555;padding:12px 0;border-bottom:1px solid var(--line)}
.features li:last-child{border-bottom:none}
.features li.bold{font-weight:700;color:#333}
.plan .btn{left:50%;transform:translateX(-50%);width:166px;font-size:13px}
.plan .btn-dark{top:593px}
.plan .btn-outline{top:647px}
.badge{position:absolute;right:0;top:50px;width:80px;height:80px;overflow:hidden}
.badge span{position:absolute;right:-30px;top:18px;width:130px;transform:rotate(45deg);background:var(--blue);color:#fff;font-family:"Montserrat",sans-serif;font-size:10px;font-weight:700;line-height:20px}
.promo{position:absolute;top:876px;left:0;width:100%;text-align:center;font-size:14px;color:#333}
.promo svg{vertical-align:-2px;margin-right:8px}

/* how it works */
.how .section-title{position:absolute;top:1516px;left:0;width:1200px}
.rule{position:absolute;height:3px;background:var(--blue);width:80px}
.step{position:absolute;width:320px;text-align:center}
.step svg{display:block;margin:0 auto}
.step h3{font-family:"Montserrat",sans-serif;font-weight:500;font-size:24px;color:var(--blue);margin-top:22px}
.step p{font-size:14.5px;line-height:23px;color:#555;margin-top:12px;padding:0 30px}

/* member banner */
.member{top:1889px;left:0;width:1200px;height:360px;background:linear-gradient(90deg,#3d3d3d 0%,#262626 50%,#1a1a1a 100%)}
.member-art{position:absolute;left:74px;top:0;width:680px;height:360px;background:linear-gradient(90deg,rgba(230,230,230,.9) 0%,rgba(120,135,150,.5) 25%,rgba(80,95,115,.35) 70%,rgba(40,40,40,0) 100%)}
.member h2{position:absolute;right:74px;top:44px;font-family:"Montserrat",sans-serif;font-weight:500;font-size:34px;color:#fff}
.member .rule{left:966px;top:102px;width:160px}
.member .from{position:absolute;right:74px;top:122px;font-family:"Montserrat",sans-serif;font-size:22px;font-weight:500;color:#fff}
.member .big{position:absolute;right:74px;top:160px;font-family:"Montserrat",sans-serif;color:#fff;font-weight:700;display:flex;align-items:flex-start}
.member .big sup{font-size:30px;line-height:36px}
.member .big b{font-size:56px;line-height:62px}
.member .big em{font-style:normal;font-size:26px;font-weight:600;margin-top:26px;margin-left:4px}

/* features */
.feature-card{position:absolute;top:2385px;width:243px;height:248px;background:var(--card);text-align:center}
.feature-card svg{display:block;margin:38px auto 0}
.feature-card h4{font-family:"Montserrat",sans-serif;font-weight:500;font-size:18px;color:var(--blue);margin-top:20px}
.feature-card p{font-size:14px;line-height:21px;color:#444;margin-top:8px;padding:0 22px}
.carousel-dots{position:absolute;top:2676px;left:585px;display:flex;gap:8px}
.carousel-dots i{width:9px;height:9px;border-radius:50%;background:#bbb}
.carousel-dots i:first-child{background:var(--blue)}

/* benefits */
.benefits{top:2742px;left:0;width:1200px;height:389px;background:linear-gradient(100deg,var(--blue-deep) 0%,var(--blue) 50%,var(--blue-light) 100%)}
.benefits h2{position:absolute;left:74px;top:118px;font-family:"Montserrat",sans-serif;font-weight:500;font-size:36px;line-height:45px;color:#fff}
.benefits .rule{left:74px;top:262px;width:150px;background:#fff}
.benefits-photo{position:absolute;left:421px;top:18px;width:325px;height:371px;background:linear-gradient(180deg,#b8d3f2 0%,#e9eef4 45%,#2a2f3a 100%);border-radius:160px 160px 0 0}
.benefit-list{position:absolute;left:793px;top:74px;list-style:none;color:#fff;font-size:14px}
.benefit-list li{height:49px;display:flex;align-items:center;gap:14px}
.benefits .btn{left:793px;top:263px;width:191px;font-size:13px}

/* footer */
.footer{top:3131px;left:0;width:1200px;height:514px;background:#fff}
.footer .brand{left:74px;top:52px;color:var(--blue);font-size:30px}
.footer .brand .dot{background:var(--blue)}
.about{position:absolute;left:74px;top:116px;width:300px;font-size:14px;line-height:24px;color:#555}
.col{position:absolute;top:46px;font-size:14px;color:#555}
.col h5{font-family:"Montserrat",sans-serif;font-weight:600;font-size:14px;color:var(--blue);margin-bottom:14px;letter-spacing:.3px}
.col li{list-style:none;line-height:32px}
.newsletter p{font-style:italic;line-height:20px;margin-bottom:14px}
.newsletter .field{width:241px;height:47px;border:1px solid #bbb;font-size:12px;color:#777;padding:14px}
.newsletter .btn{position:static;display:block;margin:10px 0 0 152px;width:89px;height:37px;line-height:37px;font-size:12px}
.divider{position:absolute;left:74px;top:271px;width:1052px;height:1px;background:var(--line)}
.footer .label{position:absolute;top:300px;font-family:"Montserrat",sans-serif;font-weight:600;font-size:14px;color:var(--blue)}
.seal{position:absolute}
.contact-line{position:absolute;left:838px;display:flex;align-items:center;gap:18px;font-family:"Montserrat",sans-serif;font-weight:600;font-size:20px;color:var(--black)}

.bottom{top:3645px;left:0;width:1200px;height:74px;background:var(--blue)}
.bottom p{position:absolute;left:74px;top:29px;font-size:12px;color:#e4efff}
.socials{position:absolute;right:74px;top:25px;display:flex;gap:16px}
.socials i{width:22px;height:22px;border-radius:50%;background:#fff}
</style>
</head>
<body>

<header class="abs topbar">
  <div class="contact">
    <span><svg width="14" height="14" viewBox="0 0 24 24"><path fill="#fff" d="M6.6 10.8a15 15 0 0 0 6.6 6.6l2.2-2.2a1 1 0 0 1 1-.25 11.4 11.4 0 0 0 3.6.57 1 1 0 0 1 1 1V20a1 1 0 0 1-1 1A17 17 0 0 1 3 4a1 1 0 0 1 1-1h3.5a1 1 0 0 1 1 1c0 1.25.2 2.45.57 3.57a1 1 0 0 1-.25 1z"/></svg>CALL US: (888) 555-0142</span>
    <span><svg width="15" height="12" viewBox="0 0 24 18"><rect x="1" y="1" width="22" height="16" rx="2" fill="none" stroke="#fff" stroke-width="2"/><path d="M1 2l11 8 11-8" fill="none" stroke="#fff" stroke-width="2"/></svg>info@brightdesk.com</span>
  </div>
  <div class="lang"><svg width="13" height="13" viewBox="0 0 24 24"><circle cx="12" cy="12" r="10" fill="var(--blue)"/></svg>EN ⌄</div>
  <div class="login">LOG IN</div>
</header>

<section class="abs hero">
  <div class="hero-photo" role="img" aria-label="Smiling support technician on the phone giving a thumbs up beside a desktop computer"></div>
  <h1>DEDICATED SUPPORT<span class="accent">ANYTIME. ANYWHERE.</span></h1>
  <div class="btn btn-dark" style="left:74px;top:302px;width:169px">GET HELP NOW!</div>
  <div class="btn btn-outline" style="left:253px;top:302px;width:166px">LEARN MORE</div>
  <div class="hero-dots"><i></i><i></i><i></i><i></i></div>
</section>

<nav class="abs nav">
  <div class="brand"><span class="dot"></span>brightdesk</div>
  <div class="menu"><a class="active">HOME</a><a>ABOUT US</a><a>SERVICES</a><a>CONTACT US</a><a>FAQS</a></div>
</nav>

<section class="abs pricing">
  <h2 class="section-title">MEMBERSHIP PRICING AND PLANS</h2>
  <div class="plans">
    <div class="plan" style="width:310px">
      <div class="plan-head">PREMIUM</div>
      <div class="plan-photo" role="img" aria-label="Support agent with headset working at a computer"></div>
      <div class="price"><sup>$</sup><b>19.99</b><em>Monthly</em></div>
      <div class="setup">$249-$300 Setup Free</div>
      <ul class="features"><li>Regular 90-Day Optimization</li><li class="bold">Unlimited 24/7 Tier 3</li><li class="bold">Technician Support</li></ul>
      <div class="btn btn-dark">ADD TO CART</div>
      <div class="btn btn-outline">VIEW MORE</div>
    </div>
    <div class="plan" style="width:360px">
      <div class="plan-head">PREMIUM PLUS</div>
      <div class="plan-photo" role="img" aria-label="Team of support agents with headsets in a call centre"></div>
      <div class="price"><sup>$</sup><b>29.99</b><em>Monthly</em></div>
      <div class="setup">$249-$300 Setup Free</div>
      <ul class="features"><li>Regular 90-Day Optimization</li><li class="bold">Unlimited 24/7 Tier 3</li><li class="bold">Technician Support</li></ul>
      <div class="btn btn-dark">ADD TO CART</div>
      <div class="btn btn-outline">VIEW MORE</div>
    </div>
    <div class="plan" style="width:312px">
      <div class="plan-head">PLATINUM</div>
      <div class="plan-photo" role="img" aria-label="Technician with headset at a computer workstation"></div>
      <div class="badge"><span>POPULAR</span></div>
      <div class="price"><sup>$</sup><b>39.99</b><em>Monthly</em></div>
      <div class="setup">$249-$300 Setup Free</div>
      <ul class="features"><li>Regular 90-Day Optimization</li><li class="bold">Unlimited 24/7 Tier 3</li><li class="bold">Technician Support</li><li>Online Identity Theft Protection</li></ul>
      <div class="btn btn-dark">ADD TO CART</div>
      <div class="btn btn-outline">VIEW MORE</div>
    </div>
  </div>
  <p class="promo"><svg width="13" height="11" viewBox="0 0 14 11"><path d="M1 6l4 4 8-9" fill="none" stroke="var(--blue)" stroke-width="2.5"/></svg>FREE Optimization and Diagnostic when you call in. Limited time offer.</p>
</section>

<section class="how">
  <h2 class="section-title">HOW IT WORKS</h2>
  <div class="rule" style="left:560px;top:1561px"></div>
  <div class="step" style="left:80px;top:1622px">
    <svg width="60" height="60" viewBox="0 0 24 24"><path d="M19 8a8 8 0 0 0-14.2 1.5M5 16a8 8 0 0 0 14.2-1.5" fill="none" stroke="#333" stroke-width="2.6"/><path d="M20.5 3v6h-6z M3.5 21v-6h6z" fill="#333"/></svg>
    <h3>FREE Diagnostic</h3>
    <p>Get a diagnostic. FOR FREE! Get a free consultation with our staff.</p>
  </div>
  <div class="step" style="left:440px;top:1622px">
    <svg width="60" height="60" viewBox="0 0 24 24"><path d="M2 10h4v11H2z M8 21V10l4-8c1.5 0 2.5 1 2.3 2.7L13.6 9H20a2 2 0 0 1 2 2.3l-1.4 7.9A2 2 0 0 1 18.6 21z" fill="#333"/></svg>
    <h3>Get Fixed</h3>
    <p>Get fixed. IMMEDIATELY! Our staff will solve your computer issues right before your eyes.</p>
  </div>
  <div class="step" style="left:800px;top:1622px">
    <svg width="66" height="60" viewBox="0 0 26 22"><path d="M7 19a6 6 0 0 1-.6-12A8 8 0 0 1 21.5 9 5 5 0 0 1 20 19z" fill="#333"/><path d="M13 16V10m-3 3l3-3 3 3" fill="none" stroke="#fff" stroke-width="2"/></svg>
    <h3>Backup your information!</h3>
    <p>Saving your files is now EASY! You will be able to retain your personal files without any loss of data.</p>
  </div>
</section>

<section class="abs member">
  <div class="member-art" role="img" aria-label="Smiling support agent with thumbs up beside a world map linked by customer portraits across continents"></div>
  <h2>Become a Member Today!</h2>
  <div class="rule"></div>
  <div class="from">Starting At Only</div>
  <div class="big"><sup>$</sup><b>19.99</b><em>Month</em></div>
  <div class="btn btn-blue" style="left:962px;top:245px;width:166px">GET STARTED</div>
</section>

<section class="features-section">
  <h2 class="section-title abs" style="top:2283px;left:0;width:1200px">ALL THE BEST FEATURES, AT THE BEST PRICE!</h2>
  <div class="rule" style="left:560px;top:2329px"></div>
  <div class="feature-card" style="left:74px">
    <svg width="80" height="56" viewBox="0 0 40 28"><rect x="6" y="2" width="28" height="19" rx="1.5" fill="none" stroke="#333" stroke-width="2.4"/><path d="M1 24h38v2H1z" fill="#333"/><circle cx="20" cy="11.5" r="5.5" fill="none" stroke="#333" stroke-width="2"/><path d="M16 15.5l8-8" stroke="#333" stroke-width="2"/></svg>
    <h4>Ad Blocker</h4>
    <p>Avoid unwanted Pop-ups with the newest Ad Blocking technology.</p>
  </div>
  <div class="feature-card" style="left:345px">
    <svg width="76" height="56" viewBox="0 0 38 28"><path d="M2 5h34M2 14h34M2 23h34" stroke="#333" stroke-width="2.4"/><rect x="8" y="1" width="6" height="8" fill="#333"/><rect x="22" y="10" width="6" height="8" fill="#333"/><rect x="12" y="19" width="6" height="8" fill="#333"/></svg>
    <h4>Regular Tune-Ups</h4>
    <p>Get a Regular Tune-Up and Optimization every 90 days.</p>
  </div>
  <div class="feature-card" style="left:612px">
    <svg width="50" height="60" viewBox="0 0 20 24"><path d="M1 1h12l6 6v16H1z" fill="#333"/><path d="M13 1v6h6" fill="#fff" opacity=".5"/><path d="M5 12h10M5 15h10M5 18h10" stroke="#fff" stroke-width="1.3"/></svg>
    <h4>System Reports</h4>
    <p>Stay up to date with Real-Time System Reporting.</p>
  </div>
  <div class="feature-card" style="left:883px">
    <svg width="70" height="60" viewBox="0 0 28 24"><rect x="10" y="1" width="8" height="6" fill="#333"/><rect x="1" y="17" width="7" height="6" fill="#333"/><rect x="10.5" y="17" width="7" height="6" fill="#333"/><rect x="20" y="17" width="7" height="6" fill="#333"/><path d="M14 7v10M4.5 17v-5h19v5" fill="none" stroke="#333" stroke-width="1.8"/></svg>
    <h4>Multiple Devices</h4>
    <p>Get support for up to 4 multiple devices. Ask about our Family Plans.</p>
  </div>
  <div class="carousel-dots"><i></i><i></i></div>
</section>

<section class="abs benefits">
  <h2>Real-Time Support<br>Features and<br>BENEFITS</h2>
  <div class="rule"></div>
  <div class="benefits-photo" role="img" aria-label="Smiling support agent wearing a headset"></div>
  <ul class="benefit-list">
    <li><svg width="13" height="11" viewBox="0 0 14 11"><path d="M1 6l4 4 8-9" fill="none" stroke="#fff" stroke-width="2.5"/></svg>24/7 Real-Time Technician Support</li>
    <li><svg width="13" height="11" viewBox="0 0 14 11"><path d="M1 6l4 4 8-9" fill="none" stroke="#fff" stroke-width="2.5"/></svg>The best Security Software in the market</li>
    <li><svg width="13" height="11" viewBox="0 0 14 11"><path d="M1 6l4 4 8-9" fill="none" stroke="#fff" stroke-width="2.5"/></svg>Regular tune-ups and optimization</li>
    <li><svg width="13" height="11" viewBox="0 0 14 11"><path d="M1 6l4 4 8-9" fill="none" stroke="#fff" stroke-width="2.5"/></svg>Setup and installation included</li>
  </ul>
  <div class="btn btn-dark">BECOME A MEMBER</div>
</section>

<footer class="abs footer">
  <div class="brand"><span class="dot"></span>brightdesk</div>
  <p class="about">We are a group of technicians who work round the clock to ensure that your PC works perfectly. Get your computer free of suspicious software and have a healthy system.</p>
  <div class="col" style="left:466px"><h5>SITE MAP</h5><ul><li>Home</li><li>About Us</li><li>Services</li><li>Contact Us</li><li>Faqs</li></ul></div>
  <div class="col" style="left:657px"><h5>PLANS</h5><ul><li>Premium Plan</li><li>Premium Plus Plan</li><li>Platinum Plan</li></ul></div>
  <div class="col newsletter" style="left:885px"><h5>NEWSLETTER SIGNUP</h5><p>Sign up for our<br>regular informational newsletters</p><div class="field">Enter Email Address</div><div class="btn btn-dark">SIGN UP</div></div>
  <div class="divider"></div>
  <div class="label" style="left:74px">TRUSTED BY</div>
  <div class="seal" style="left:80px;top:338px;width:150px;height:126px;border-radius:50%;background:radial-gradient(circle,#e8c25a 0%,#b88a1e 100%)"></div>
  <div class="seal" style="left:268px;top:340px;width:120px;height:122px;border-radius:12px;background:#c62828"></div>
  <div class="seal" style="left:474px;top:368px;width:120px;height:48px;border-radius:4px;background:#1f9d55"></div>
  <div class="label" style="left:838px">CONTACT US</div>
  <div class="contact-line" style="top:348px"><svg width="24" height="24" viewBox="0 0 24 24"><path fill="#111" d="M6.6 10.8a15 15 0 0 0 6.6 6.6l2.2-2.2a1 1 0 0 1 1-.25 11.4 11.4 0 0 0 3.6.57 1 1 0 0 1 1 1V20a1 1 0 0 1-1 1A17 17 0 0 1 3 4a1 1 0 0 1 1-1h3.5a1 1 0 0 1 1 1c0 1.25.2 2.45.57 3.57a1 1 0 0 1-.25 1z"/></svg>(888) 555-0142</div>
  <div class="contact-line" style="top:396px"><svg width="24" height="20" viewBox="0 0 24 20"><rect x="1" y="1" width="22" height="18" rx="2" fill="#111"/><path d="M2 3l10 8 10-8" fill="none" stroke="#fff" stroke-width="2"/></svg>info@brightdesk.com</div>
</footer>

<div class="abs bottom">
  <p>Copyright © 2017. All rights reserved. Terms and Conditions - Refund Policy - Privacy Policy</p>
  <div class="socials"><i></i><i></i><i></i><i></i><i></i></div>
</div>

</body>
</html>
```